PEACFUL ACUPUNCTURE PRACTITIONER NEEDS A NEW COAT

I need a new design for an exiting website http://willowgateneedlework.com/ for a acupuncturist. This will be a minimalism design with lots and lots of white space. Home page and one interior page. Please keep the feeling of calm and peaceful serenity. For Color scheme: https://www.morningfernclinic.com/fertility. The bottom part of the home page with sections and links to the service pages: https://harborlotuswellness.com/. The client likes this the best: http://mfclinic.com/. I'm attaching the logo and content pages.

Target Market(s)

Women

Industry/Entity Type

Wellness, health, wellbeing, meditation

Number of Pages Required

2 page

Font styles to use
Sans Serif
Decorative

Colors

Designer to choose colors to be used in the design.

Requirements
Must have
Nice to have
• Follow new website drafts and links
Should not have
• Busy with bright colors. No poping

```html
<!DOCTYPE html>
<html lang="en">
<head>
<meta charset="utf-8">
<title>Willow Gate Acupuncture</title>
<link href="https://fonts.googleapis.com/css2?family=Cormorant+Garamond:wght@500&family=Jost:wght@300;400&display=swap" rel="stylesheet">
<style>
:root{
  --cream:#fbf2e1;
  --cream-deep:#f6e6c8;
  --blob:#faf1e3;
  --gold:#b99869;
  --gold-light:#caa97c;
  --rose:#a7767f;
  --text:#6f655d;
  --muted:#9a8f86;
  --white:#ffffff;
}
*{margin:0;padding:0;box-sizing:border-box}
html,body{width:1200px;height:4215px;overflow:hidden;background:var(--white)}
body{position:relative;font-family:"Jost",sans-serif;font-weight:300;color:var(--text)}
.abs{position:absolute}
.serif{font-family:"Cormorant Garamond",serif;font-weight:500}
.hero-bg{left:0;top:0;width:1200px;height:600px}
.brand{left:126px;top:40px;display:flex;align-items:center;gap:8px}
.brand-dot{width:16px;height:16px;border-radius:50%;background:var(--rose);opacity:.7}
.brand-name{font-family:"Cormorant Garamond",serif;font-weight:500;font-size:17px;color:var(--rose)}
.nav{left:286px;top:44px;display:flex;gap:27px;font-size:13.5px;color:var(--muted)}
.hero-title{left:124px;top:215px;font-size:36px;line-height:42px;color:var(--gold);white-space:nowrap}
.hero-text{left:124px;top:306px;width:490px;font-size:14px;line-height:18px}
.btn{background:var(--rose);color:var(--white);font-size:13px;border-radius:12px;padding:3px 14px}
.hero-btn{left:124px;top:374px}
.ph{border-radius:4px}
.hero-photo{left:660px;top:115px;width:400px;height:458px;background:linear-gradient(180deg,#f7e6e3,#f0c9cb);border-radius:200px 200px 0 0}
.section-title{left:0;width:1200px;top:716px;text-align:center;font-size:28px;color:var(--gold);letter-spacing:.5px}
.philo{top:776px;width:416px;font-size:14px;line-height:18px;text-align:justify}
.blob{background:var(--blob);border-radius:48% 52% 45% 55%/55% 45% 55% 45%}
.svc-title{font-size:26px;color:var(--gold);white-space:nowrap}
.svc-text{font-size:14px;line-height:18px;width:400px}
.more{font-size:13px;color:var(--gold-light)}
.contact-bg{left:0;top:3080px;width:1200px;height:640px}
.contact-title{left:124px;top:3325px;font-size:36px;line-height:42px;color:var(--gold);white-space:nowrap}
.contact-text{left:124px;top:3415px;width:490px;font-size:14px;line-height:18px}
.field{left:684px;width:274px;height:24px;background:var(--white);border-radius:3px;font-size:12px;color:var(--muted);padding:4px 16px}
.submit{left:686px;top:3574px}
.map{left:128px;top:3921px;width:383px;height:221px;background:linear-gradient(135deg,#eef0f2,#dfe4ea);box-shadow:0 2px 8px rgba(0,0,0,.15)}
.info{left:558px;font-size:13px;line-height:17px;color:var(--muted)}
.links{font-size:13px;line-height:28px;color:var(--muted)}
.foot-brand{left:819px;top:4076px;display:flex;align-items:center;gap:12px}
.foot-brand .brand-dot{width:40px;height:40px}
.foot-brand .brand-name{font-size:32px}
</style>
</head>
<body>

<svg class="abs hero-bg" viewBox="0 0 1200 600" aria-hidden="true">
  <path d="M0 0H1200V522C1060 540 920 585 700 578C480 570 330 530 170 524C90 521 40 520 0 530Z" fill="var(--cream)"/>
</svg>

<div class="abs brand"><span class="brand-dot"></span><span class="brand-name">Willow Gate</span></div>
<nav class="abs nav">
  <span>Home</span><span>About</span><span>Fertility &amp; Pregnancy</span><span>Hormone Balance</span><span>Strength &amp; Structure</span><span>Emotional Wellbeing</span><span>Shop</span><span>Reviews</span>
</nav>

<div class="abs ph hero-photo" role="img" aria-label="Photo of a pregnant woman in a soft pink dress, seen in profile"></div>
<h1 class="abs serif hero-title">Specializing in women’s health,<br>fertility challenges &amp; pregnancy care</h1>
<p class="abs hero-text">Get a free 30-minute consultation. We are always available to help answer any questions you may have about acupuncture or herbal medicine in a relaxed environment.</p>
<span class="abs btn hero-btn">Get a schedule</span>

<h2 class="abs serif section-title">PHILOSOPHY OF CARE</h2>
<p class="abs philo" style="left:124px">Acupuncture &amp; Chinese Herbal Medicine are rooted in over 3000 years of history and tradition. As a complete medical system that has remained flexible and relevant we honor what has worked from the past while embracing the medicine of tomorrow.</p>
<p class="abs philo" style="left:658px">At Willow Gate Acupuncture we provide compassionate, respectful and empowering care in a safe and inclusive environment. Our goal is to harmonize physical, mental and emotional wellbeing to strengthen the Willow Gate from which we all strive to live.</p>

<!-- Fertility -->
<div class="abs blob" style="left:69px;top:1085px;width:258px;height:274px"></div>
<h3 class="abs serif svc-title" style="left:133px;top:1168px">Fertility &amp; Pregnancy</h3>
<p class="abs svc-text" style="left:133px;top:1218px">At Willow Gate Acupuncture our goal is to help build families and we happily embrace the diversity that word includes. We warmly welcome the LGBTQ community, single mothers and parents by choice and surrogates.</p>
<span class="abs more" style="left:133px;top:1302px">Learn more &gt;</span>
<div class="abs ph" style="left:655px;top:1121px;width:401px;height:238px;background:radial-gradient(ellipse at 50% 45%,#eaa0a8 0 22%,#c9a47a 40%,rgba(255,255,255,0) 70%)" role="img" aria-label="Photo of a bird's nest holding pink eggs"></div>

<!-- Hormone -->
<div class="abs ph" style="left:229px;top:1563px;width:221px;height:320px;background:linear-gradient(180deg,#d9cfcb,#b3a6a1);border-radius:45% 45% 20% 20%" role="img" aria-label="Photo of a stack of balanced smooth stones"></div>
<div class="abs blob" style="left:884px;top:1572px;width:246px;height:278px"></div>
<h3 class="abs serif svc-title" style="left:673px;top:1628px">Hormone Balance</h3>
<p class="abs svc-text" style="left:673px;top:1678px;width:398px">Our hormones are constantly shifting and occasionally this internal orchestra needs to be refined. Acupuncture works to help the body rediscover the positive patterns that lead to improved health and well being. By repeating these patterns we are reminding the body how to access greater health on its own</p>
<span class="abs more" style="left:673px;top:1798px">Learn more &gt;</span>

<!-- Strength -->
<div class="abs blob" style="left:69px;top:2087px;width:258px;height:278px"></div>
<h3 class="abs serif svc-title" style="left:133px;top:2170px">Strength &amp; Structure</h3>
<p class="abs svc-text" style="left:133px;top:2220px">Our bodies carry us through all we do. Sometimes they need attention and support. Whether you need a simple “tune up” or help recovering from surgery or illness acupuncture can help.</p>
<span class="abs more" style="left:133px;top:2304px">Learn more &gt;</span>
<div class="abs ph" style="left:737px;top:2079px;width:275px;height:336px;background:radial-gradient(ellipse at 50% 38%,#a9c97a 0 45%,rgba(255,255,255,0) 68%)" role="img" aria-label="Photo of a green leafy tree"></div>

<!-- Emotional -->
<div class="abs ph" style="left:164px;top:2529px;width:311px;height:270px;background:radial-gradient(ellipse at 50% 50%,#f1d6c6 0 40%,rgba(255,255,255,0) 70%)" role="img" aria-label="Photo of two gently open hands"></div>
<div class="abs blob" style="left:884px;top:2537px;width:246px;height:279px"></div>
<h3 class="abs serif svc-title" style="left:673px;top:2596px">Emotional Wellbeing</h3>
<p class="abs svc-text" style="left:673px;top:2646px;width:398px">Our mental and emotional wellness is imperative to whole body healing. Without the unity of heart and head other systems can suffer. Acupuncture and herbs can help reset patterns of relaxation while teaching the body to access theses resources more easily on its’ own.</p>
<span class="abs more" style="left:673px;top:2747px">Learn more &gt;</span>

<!-- Contact -->
<svg class="abs contact-bg" viewBox="0 0 1200 640" aria-hidden="true">
  <defs><linearGradient id="cg" x1="0" y1="0" x2="1" y2="1"><stop offset="0" stop-color="#fcf4e6"/><stop offset="1" stop-color="var(--cream-deep)"/></linearGradient></defs>
  <path d="M0 28C120 0 260 40 380 120C470 180 560 150 660 80C760 20 900 10 1020 40C1110 60 1170 30 1200 20V530C1120 600 900 640 700 620C480 600 300 520 160 480C80 460 30 470 0 480Z" fill="url(#cg)"/>
</svg>
<h2 class="abs serif contact-title">Get the best help for women’s health,<br>fertility challenges &amp; pregnancy care</h2>
<p class="abs contact-text">Get a free 30-minute consultation. We are always available to help answer any questions you may have about acupuncture or herbal medicine in a relaxed environment.</p>
<div class="abs field" style="top:3331px">Name</div>
<div class="abs field" style="top:3371px">Email address</div>
<div class="abs field" style="top:3411px">Subject</div>
<div class="abs field" style="top:3451px;height:93px">Message</div>
<span class="abs btn submit">Submit</span>

<!-- Footer -->
<div class="abs ph map" role="img" aria-label="Street map showing the clinic location"></div>
<p class="abs info" style="top:3924px">48 Alder Row<br>Easthaven, MA 01099<br>mara@willowgateneedlework.com<br>555-014-2280</p>
<p class="abs info" style="top:4018px">Tuesday — Friday 10am - 6pm<br>Saturday 10am - 3pm</p>
<p class="abs info" style="top:4100px">Treatments are by appointment only.<br>Please call or email to schedule.</p>
<div class="abs links" style="left:819px;top:3916px">Home<br>About Mara<br>Fertility &amp; Pregnancy<br>Hormone Balance</div>
<div class="abs links" style="left:956px;top:3916px">Strength &amp; Structure<br>Emotional Wellbeing<br>Online Shop<br>Testimonials</div>
<div class="abs foot-brand"><span class="brand-dot"></span><span class="brand-name">Willow Gate</span></div>

</body>
</html>
```